Business cards in digital learning for freelancer

Hello, I need a business cards in french. I work in the Digital learning industries as freeelancer; I'm an expert in digital learning. I work in France. My customer are in the health industry, pharmaceutical industry, and training organization. I've got a logo. I offer three services: consulting, Design, and Training. In the consulting, I offers coaching to choose your digital learning tools and the digital learning strategy. For the Design, I product differents level of elearning like rapid-learning, elearning, micro-learning, video-learning. And for the training service, I've create training about pedagogy, digital learning management project, Digital learning design.
I join my Logo create in this platform. My universe is gamified. I like the life, and I'm very social. I want a card like I'm I. I love Art (painting), Europeen comics. I use in my visual support "permanent maker" font and caracters. I would like cards: elegant, modern, Top class. If you need any information, you can ask me.
thanks for ideas

Target Market(s)

in health industries and training organization for Training manager, instructor, human resources director

Contact Information for Business Card

Phone number : 06 31 87 59 14 , mail: lucienmorvaltes@courriel-nord.fr, web: lucienmorvaltes.fr , LinkedIn

Font styles to use
Sans Serif

Requirements
Must have
• Use my logo and write my 3 services (consulting, training, design)

```html
<!DOCTYPE html>
<html lang="fr">
<head>
<meta charset="UTF-8">
<title>Cartes de visite – Lucien Morvaltes</title>
<link rel="stylesheet" href="https://fonts.googleapis.com/css2?family=Montserrat:wght@400;600;700&family=Open+Sans:wght@400;600&display=swap">
<style>
  :root {
    --bg: #2b2b2d;
    --card-grey: #5d5e60;
    --card-grey-dark: #4a4b4d;
    --card-white: #ffffff;
    --orange: #f07a22;
    --ink-grey: #6b6b6d;
    --text-light: #f2f2f2;
    --illustration-warm: #e9c9a8;
    --illustration-cool: #cfcfd2;
  }
  * { box-sizing: border-box; margin: 0; padding: 0; }
  html, body { width: 1200px; height: 898px; overflow: hidden; }
  body {
    background: var(--bg);
    font-family: "Open Sans", Arial, sans-serif;
    position: relative;
  }
  .card {
    position: absolute;
    top: 274px;
    width: 540px;
    height: 350px;
    border-radius: 26px;
    overflow: hidden;
  }
  .card--front { left: 40px; background: var(--card-white); }
  .card--back { left: 620px; background: var(--card-grey); }

  /* Front */
  .illustration {
    position: absolute;
    border-radius: 18px;
  }
  .illustration--host {
    left: 24px; top: 22px; width: 92px; height: 100px;
    background: linear-gradient(180deg, var(--illustration-warm), #3b3b3d);
  }
  .illustration--team {
    right: 26px; top: 150px; width: 230px; height: 120px;
    background: linear-gradient(90deg, #f2b58a, #e3c14f 50%, #6e9a4b);
  }
  .front-mark {
    position: absolute;
    left: 150px; top: 34px;
    display: flex; align-items: center; gap: 10px;
  }
  .front-mark__dot {
    width: 22px; height: 22px; border-radius: 50%;
    background: var(--orange);
  }
  .front-mark__name {
    font-family: "Montserrat", Arial, sans-serif;
    font-weight: 600; font-size: 18px; color: var(--orange);
  }
  .identity {
    position: absolute;
    left: 150px; top: 92px;
  }
  .identity__name {
    font-family: "Montserrat", Arial, sans-serif;
    font-weight: 700; font-size: 24px; letter-spacing: 1px;
    color: var(--ink-grey); text-transform: uppercase;
  }
  .identity__role {
    font-family: "Montserrat", Arial, sans-serif;
    font-size: 16px; color: var(--orange); margin-top: 2px;
  }
  .contact-band {
    position: absolute; left: 0; bottom: 0;
    width: 540px; height: 130px;
  }
  .contacts {
    position: absolute; left: 0; bottom: 14px; width: 540px;
    display: flex; justify-content: space-around; align-items: flex-end;
    padding: 0 14px;
  }
  .contact {
    display: flex; flex-direction: column; align-items: center; gap: 8px;
    color: var(--text-light); font-size: 12.5px;
  }
  .contact__icon {
    width: 30px; height: 30px; border-radius: 50%;
    background: var(--card-grey-dark);
    border: 2px solid #7a7b7d;
    display: flex; align-items: center; justify-content: center;
  }

  /* Back */
  .back-content {
    position: absolute; inset: 0;
    display: flex; flex-direction: column; align-items: center; justify-content: center;
    gap: 18px;
  }
  .back-mark { display: flex; align-items: center; gap: 14px; }
  .back-mark__dot {
    width: 40px; height: 40px; border-radius: 50%; background: var(--orange);
  }
  .back-mark__name {
    font-family: "Montserrat", Arial, sans-serif;
    font-weight: 400; font-size: 30px; color: var(--text-light);
  }
  .services {
    font-family: "Montserrat", Arial, sans-serif;
    font-size: 17px; color: var(--text-light); letter-spacing: 0.5px;
  }
  .services__sep { color: var(--orange); margin: 0 6px; }
</style>
</head>
<body>

<section class="card card--front" aria-label="Recto de la carte">
  <div class="illustration illustration--host" role="img" aria-label="Illustration d'une formatrice dessinée"></div>

  <div class="front-mark">
    <span class="front-mark__dot"></span>
    <span class="front-mark__name">Atelier Morvaltes</span>
  </div>

  <div class="identity">
    <p class="identity__name">Lucien Morvaltes</p>
    <p class="identity__role">Digital learning consultant</p>
  </div>

  <div class="illustration illustration--team" role="img" aria-label="Illustration de trois apprenants dessinés"></div>

  <svg class="contact-band" viewBox="0 0 540 130" preserveAspectRatio="none" aria-hidden="true">
    <path d="M0 40 Q270 -10 540 40 L540 130 L0 130 Z" fill="var(--card-grey)"/>
    <path d="M0 34 Q270 -16 540 34" fill="none" stroke="var(--orange)" stroke-width="3"/>
  </svg>

  <ul class="contacts" style="list-style:none">
    <li class="contact">
      <span class="contact__icon">
        <svg width="14" height="14" viewBox="0 0 24 24"><path fill="var(--orange)" d="M6.6 10.8a15 15 0 0 0 6.6 6.6l2.2-2.2c.3-.3.7-.4 1-.2 1.1.4 2.3.6 3.6.6.6 0 1 .4 1 1V20c0 .6-.4 1-1 1A17 17 0 0 1 3 4c0-.6.4-1 1-1h3.5c.6 0 1 .4 1 1 0 1.3.2 2.5.6 3.6.1.3 0 .7-.2 1z"/></svg>
      </span>
      <span>06 31 87 59 14</span>
    </li>
    <li class="contact">
      <span class="contact__icon">
        <svg width="14" height="14" viewBox="0 0 24 24"><rect x="3" y="5" width="18" height="14" rx="2" fill="var(--orange)"/><path d="M3 7l9 6 9-6" fill="none" stroke="var(--card-grey-dark)" stroke-width="2"/></svg>
      </span>
      <span>lucienmorvaltes@courriel-nord.fr</span>
    </li>
    <li class="contact">
      <span class="contact__icon">
        <svg width="14" height="14" viewBox="0 0 24 24"><circle cx="12" cy="12" r="9" fill="none" stroke="var(--orange)" stroke-width="2"/><path d="M3 12h18M12 3c3 3 3 15 0 18M12 3c-3 3-3 15 0 18" fill="none" stroke="var(--orange)" stroke-width="1.6"/></svg>
      </span>
      <span>lucienmorvaltes.fr</span>
    </li>
  </ul>
</section>

<section class="card card--back" aria-label="Verso de la carte">
  <div class="back-content">
    <div class="back-mark">
      <span class="back-mark__dot"></span>
      <span class="back-mark__name">Atelier Morvaltes</span>
    </div>
    <p class="services">consulting<span class="services__sep">|</span>training<span class="services__sep">|</span>design</p>
  </div>
</section>

</body>
</html>
```